Business card for auto dealership

Looking for a clean modern design.
Would like attached logo incorporated

Industry/Entity Type

Car dealership

Contact Information for Business Card

Name, website, phone, cell, fax, email

```html
<!DOCTYPE html>
<html lang="en">
<head>
<meta charset="utf-8">
<title>Halvorsen Truck &amp; Auto Sales – Business Card</title>
<link href="https://fonts.googleapis.com/css2?family=Montserrat:wght@400;500;700;800&display=swap" rel="stylesheet">
<style>
  :root {
    --ink: #111111;
    --paper: #ffffff;
    --backdrop: #d6d6d6;
    --muted: #2a2a2a;
  }
  * { box-sizing: border-box; margin: 0; padding: 0; }
  html, body { width: 1200px; height: 1059px; overflow: hidden; }
  body {
    background: var(--backdrop);
    font-family: "Montserrat", Arial, sans-serif;
    display: flex; flex-direction: column; align-items: center; justify-content: center;
    gap: 60px;
  }
  .card {
    position: relative;
    width: 760px; height: 434px;
    border-radius: 4px;
    overflow: hidden;
    box-shadow: 0 10px 30px rgba(0,0,0,.25);
  }
  .card--back { background: var(--ink); color: var(--paper); display: flex; align-items: center; justify-content: center; }
  .card--front { background: var(--paper); color: var(--ink); }

  .brand { display: flex; flex-direction: column; align-items: flex-start; font-weight: 800; line-height: 1; }
  .brand__name { font-size: 64px; letter-spacing: -1px; }
  .brand__tag { font-size: 15px; letter-spacing: 1.5px; margin-top: 6px; margin-left: 4px; }
  .card--back .brand__name { font-size: 84px; }
  .card--back .brand__tag { font-size: 19px; }

  .card--front .brand { position: absolute; right: 48px; top: 118px; }
  .card--front .brand__name { font-size: 52px; }
  .card--front .brand__tag { font-size: 12px; }

  .wave { position: absolute; inset: 0; width: 100%; height: 100%; }

  .contact { position: absolute; left: 52px; top: 170px; }
  .contact__name {
    font-weight: 700; font-size: 21px; letter-spacing: .5px;
    padding-bottom: 8px; border-bottom: 2px solid var(--ink);
    display: inline-block; padding-right: 20px;
  }
  .contact__list { list-style: none; margin-top: 14px; }
  .contact__item { display: flex; align-items: center; gap: 10px; font-size: 17px; color: var(--muted); line-height: 27px; }
  .contact__icon { width: 15px; height: 15px; fill: var(--ink); flex: none; }
</style>
</head>
<body>

<section class="card card--back">
  <div class="brand">
    <span class="brand__name">Halvorsen</span>
    <span class="brand__tag">TRUCK &amp; AUTO SALES</span>
  </div>
</section>

<section class="card card--front">
  <svg class="wave" viewBox="0 0 760 434" preserveAspectRatio="none" aria-hidden="true">
    <path d="M760,232 C610,250 520,330 400,385 C330,415 270,428 230,434 L760,434 Z" fill="var(--ink)"/>
    <path d="M760,196 C600,212 500,300 380,360 C320,390 260,404 220,408 C270,400 330,382 390,350 C510,288 610,222 760,212 Z" fill="var(--ink)"/>
  </svg>

  <div class="brand">
    <span class="brand__name">Halvorsen</span>
    <span class="brand__tag">TRUCK &amp; AUTO SALES</span>
  </div>

  <div class="contact">
    <h1 class="contact__name">DANA HALVORSEN</h1>
    <ul class="contact__list">
      <li class="contact__item">
        <svg class="contact__icon" viewBox="0 0 16 16"><path d="M3 1l3 3-2 2c1 2 3 4 5 5l2-2 3 3-2 3C6 14 2 10 1 3z"/></svg>555-014-2291
      </li>
      <li class="contact__item">
        <svg class="contact__icon" viewBox="0 0 16 16"><path d="M4 0h8a1 1 0 011 1v14a1 1 0 01-1 1H4a1 1 0 01-1-1V1a1 1 0 011-1zm1 2v10h6V2z"/></svg>555-017-3382
      </li>
      <li class="contact__item">
        <svg class="contact__icon" viewBox="0 0 16 16"><path d="M4 0h8v5H4zM1 6h14v7h-3v3H4v-3H1zm5 5v3h4v-3z"/></svg>555-019-4476
      </li>
      <li class="contact__item">
        <svg class="contact__icon" viewBox="0 0 16 16"><path d="M0 3h16v1L8 9 0 4zm0 3l8 5 8-5v7H0z"/></svg>dana@halvorsenauto.com
      </li>
      <li class="contact__item">
        <svg class="contact__icon" viewBox="0 0 16 16"><path d="M8 0a8 8 0 100 16A8 8 0 008 0zm0 1.5c1 1.2 1.7 3 1.9 5.5H6.1C6.3 4.5 7 2.7 8 1.5zM1.6 7h3C4.7 5 5.2 3.4 5.9 2A6.5 6.5 0 001.6 7zm0 2a6.5 6.5 0 004.3 5c-.7-1.4-1.2-3-1.3-5zm4.5 0h3.8c-.2 2.5-.9 4.3-1.9 5.5C7 13.3 6.3 11.5 6.1 9zm5.3 0h3a6.5 6.5 0 01-4.3 5c.7-1.4 1.2-3 1.3-5zm3-2h-3c-.1-2-.6-3.6-1.3-5a6.5 6.5 0 014.3 5z"/></svg>Halvorsenauto.com
      </li>
    </ul>
  </div>
</section>

</body>
</html>
```